Form Crafters Business Card

Professional cosmetic surgery company, based in very exclusive area in London. High profiled clientele. Brand is very artistic, modern, state-of-the-art, safe. The best in the business. Celebrity clientele.

Form Crafter’s of London is a brand serving a discriminating and exclusive clientele who value personal service that is both intimate and high end. Our clients choose Form Crafters because of the relationships we share with all of our customers. The clients of Form Crafters have an equal partnership between customers, and very experienced, highly qualified medical professionals. This together provides you with a professional service that keeps you looking good and feeling good. It is a relationship based on honesty, compassion, loyalty and respect.
Form Crafter’s have provided services for internationally recognised celebrities, and other high profiled individuals.

The cards are used for networking at private, exclusive events with VIPs.

Target Market(s)

Professionals
Rich people

Industry/Entity Type

Professional Service

Contact Information for Business Card

Need double sided business card design for 4 people. Back of the business card needs to have contrast background to the front with butterfly watermark with services provided:
Hair Restoration surgery
Hair Loss treatments
Breast surgery
Rhinoplasty
Sonix Liposuction
Fat Grafting
Relaxin & Fillers

Front of the business card needs to be a nice satin black.
with following information:
Tavish Kolendran - name
Chief Executive - Job title

www.formcrafters.co.uk
tavish@formcrafters.co.uk
Phone: +44 (0)207 461 2295
Mobile: +44 (0)7912 548 237

The London Ashcombe Clinic
14 Ashcombe Street | London | W1K 3PQ
Off Tolland Street

All business cards have the same address, phone, website as Tavish's details.
Same details on the back of the business card as well.
The other cards have different name, job title, email, mobile number

Faraz Qureshi - Name
Partner - Job Title
Former England International Cricketer - please include below job title

email: faraz@formcrafters.co.uk
mobile: +44(0)7846 205318

Dr Tadeu Varella - Name
Plastic Surgeon - Job Title
drvarella@formcrafters.co.uk
No mobile number

Dr Zain Hussaini FRCS (please put FRCS in small font) - Name
Hair Restoration Surgeon - Job Title
drhussaini@formcrafters.co.uk
No mobile number

Colors
cedeec
85abd2
0655a3

Requirements
Must have
• The logo needs to be in a metallic finish
• Text needs to be striking
• nice background
• butterfly watermark on the back

```html
<!DOCTYPE html>
<html lang="en">
<head>
<meta charset="utf-8">
<title>Form Crafters Business Card</title>
<link href="https://fonts.googleapis.com/css2?family=Arimo:wght@400;700&family=Tinos&display=swap" rel="stylesheet">
<style>
  :root {
    --backdrop: #e9e6e1;
    --satin-black: #0b0b0b;
    --satin-edge: #1c1c1c;
    --white: #f4f4f4;
    --accent-orange: #f08a1c;
    --brand-blue: #85abd2;
    --orange-light: #f7a53a;
    --orange-mid: #ee7d1f;
    --orange-deep: #e0581a;
    --ink: #1a0d05;
  }
  * { margin: 0; padding: 0; box-sizing: border-box; }
  html, body { width: 1200px; height: 840px; overflow: hidden; }
  body { background: var(--backdrop); position: relative; }

  .card {
    position: absolute;
    width: 560px;
    height: 320px;
    border-radius: 4px;
    box-shadow: 0 14px 30px rgba(0,0,0,0.22);
    overflow: hidden;
  }

  /* Front: satin black */
  .card-front {
    left: 580px;
    top: 110px;
    background: linear-gradient(160deg, var(--satin-edge) 0%, var(--satin-black) 55%, #050505 100%);
    font-family: "Arimo", Arial, sans-serif;
    color: var(--white);
  }
  .person { position: absolute; left: 34px; top: 36px; }
  .person-name { font-size: 21px; font-weight: 700; letter-spacing: 0.5px; }
  .person-title { font-size: 12px; color: var(--accent-orange); margin-top: 4px; }

  .contact-list { position: absolute; left: 34px; top: 104px; list-style: none; }
  .contact-item {
    display: flex; align-items: center; gap: 10px;
    font-size: 12.5px; line-height: 22px;
  }
  .contact-icon { width: 12px; height: 12px; flex: none; }

  .address {
    position: absolute; left: 34px; bottom: 28px;
    font-size: 12px; letter-spacing: 0.2px;
  }

  .brand {
    position: absolute; right: 38px; top: 118px;
    display: flex; align-items: center; gap: 10px;
  }
  .brand-dot { width: 14px; height: 14px; border-radius: 50%; background: var(--brand-blue); }
  .brand-name { font-size: 26px; font-weight: 400; color: var(--brand-blue); letter-spacing: 1px; }

  /* Back: orange services */
  .card-back {
    left: 60px;
    top: 420px;
    background: linear-gradient(135deg, var(--orange-light) 0%, var(--orange-mid) 50%, var(--orange-deep) 100%);
    font-family: "Tinos", "Times New Roman", serif;
    color: var(--ink);
  }
  .services { position: absolute; left: 48px; top: 44px; list-style: none; }
  .service { font-size: 21px; line-height: 31px; }
</style>
</head>
<body>

  <section class="card card-front" aria-label="Business card front">
    <div class="person">
      <div class="person-name">TAVISH KOLENDRAN</div>
      <div class="person-title">Chief Executive</div>
    </div>

    <ul class="contact-list">
      <li class="contact-item">
        <svg class="contact-icon" viewBox="0 0 12 12"><rect x="3" y="0.5" width="6" height="11" rx="1.2" fill="none" stroke="#f08a1c" stroke-width="1.2"/><circle cx="6" cy="9.5" r="0.8" fill="#f08a1c"/></svg>
        +44 (0)7912 548 237
      </li>
      <li class="contact-item">
        <svg class="contact-icon" viewBox="0 0 12 12"><path d="M2.5 1 L4.5 1 L5.3 3.5 L4 4.6 C4.7 6 6 7.3 7.4 8 L8.5 6.7 L11 7.5 L11 9.5 C11 10.4 10.3 11 9.5 11 C5 10.6 1.4 7 1 2.5 C1 1.7 1.6 1 2.5 1 Z" fill="#f08a1c"/></svg>
        +44 (0)207 461 2295
      </li>
      <li class="contact-item">
        <svg class="contact-icon" viewBox="0 0 12 12"><rect x="0.6" y="2" width="10.8" height="8" rx="1" fill="none" stroke="#f08a1c" stroke-width="1.2"/><path d="M1 2.5 L6 6.5 L11 2.5" fill="none" stroke="#f08a1c" stroke-width="1.2"/></svg>
        tavish@formcrafters.co.uk
      </li>
      <li class="contact-item">
        <svg class="contact-icon" viewBox="0 0 12 12"><circle cx="6" cy="6" r="5.2" fill="none" stroke="#f08a1c" stroke-width="1.2"/><path d="M0.8 6 H11.2 M6 0.8 C3.5 3.5 3.5 8.5 6 11.2 M6 0.8 C8.5 3.5 8.5 8.5 6 11.2" fill="none" stroke="#f08a1c" stroke-width="1"/></svg>
        www.formcrafters.co.uk
      </li>
    </ul>

    <div class="address">The London Ashcombe Clinic, 14 Ashcombe Street London W1K 3PQ</div>

    <div class="brand">
      <span class="brand-dot"></span>
      <span class="brand-name">Form Crafters</span>
    </div>
  </section>

  <section class="card card-back" aria-label="Business card back">
    <ul class="services">
      <li class="service">Hair Restoration surgery</li>
      <li class="service">Hair Loss treatments</li>
      <li class="service">Breast surgery</li>
      <li class="service">Rhinoplasty</li>
      <li class="service">Sonix Liposuction</li>
      <li class="service">Fat Grafting Relaxin &amp; Fillers</li>
    </ul>
  </section>

</body>
</html>
```